Conversion Landing Page - "COMPANY NAME is Endorsed By"

You may see our current radio-landing page at our company website: havenquill.com/radio-landing

Please visit the following examples:

Positive examples of elements and layouts we like:
dorvantek.com/mark

Please mock designs of a high conversion call to action inspiring action landing page highlighting the 5-year history, credibility record at QVR+ (A+), and the endorsements we have acquired from well known financial literacy figures.

Our primary use of this page is to direct PPC and Direct Radio Advertising.

I will respond within 24 hours, please send me your questions.

Target Market(s)

travel, financial services

Number of Pages Required

1 page

Font styles to use
Serif
Sans Serif

Requirements
Must have
• images or elements representing the radio show and figures endorsing out company and services.
• Some background detail on the radio show subjects that resonates most closely to the service we offer - financial wellbeing and trustworthy timeshare freedom service

```html
<!DOCTYPE html>
<html lang="en">
<head>
<meta charset="utf-8">
<title>Haven Quill – Timeshare Release</title>
<link href="https://fonts.googleapis.com/css2?family=Nunito+Sans:wght@400;600;700&display=swap" rel="stylesheet">
<style>
:root{
  --blue-dark:#0d4f8b;
  --blue:#1a78c2;
  --blue-bright:#2f8fde;
  --navy:#0b3f6e;
  --navy-deep:#082f54;
  --red:#e21b1b;
  --ink:#2b2b2b;
  --muted:#8a8a8a;
  --grey-bg:#efefef;
  --panel:#e9e9e9;
  --white:#ffffff;
  --line:#d8d8d8;
}
*{box-sizing:border-box;margin:0;padding:0}
html,body{width:1200px;height:2675px;overflow:hidden;background:var(--white)}
body{font-family:"Nunito Sans",Arial,sans-serif;color:var(--ink);position:relative}
a{color:inherit;text-decoration:none}

.site-header{position:absolute;top:0;left:0;width:1200px;height:102px;background:var(--blue-dark);display:flex;align-items:center;padding:0 110px}
.brand{display:flex;align-items:center;gap:12px;color:var(--white);font-weight:700;font-size:30px;width:265px}
.brand-square{width:34px;height:34px;background:var(--white)}
.main-nav{display:flex;gap:40px;font-size:16px;color:#d6e6f5;align-items:center}
.main-nav .active{color:var(--white);font-weight:700}
.header-phone{margin-left:auto;color:var(--white);font-weight:700;font-size:19px;display:flex;align-items:center;gap:8px}

.hero{position:absolute;top:102px;left:0;width:1200px;height:321px;background:linear-gradient(100deg,#1466b0 0%,#2286d6 55%,#1a72c0 100%);overflow:hidden}
.hero-portrait{position:absolute;left:165px;top:6px;width:240px;height:315px;background:linear-gradient(180deg,#3b4a5c 0%,#1c2430 100%)}
.hero-copy{position:absolute;left:489px;top:64px;width:560px;color:var(--white)}
.hero-copy h1{font-weight:400;font-size:34px;line-height:1.1}
.hero-copy p{font-size:15px;line-height:1.55;margin-top:14px}
.btn{display:inline-flex;align-items:center;justify-content:center;font-weight:700;text-transform:uppercase;color:var(--white)}
.btn-hero{width:172px;height:41px;background:var(--navy);font-size:13px;margin-top:18px}

.intro{position:absolute;top:423px;left:0;width:1200px;height:340px}
.quote-card{position:absolute;left:160px;top:46px;width:300px;text-align:center}
.quote-name{font-size:16px}
.quote-role{font-size:15px;color:var(--muted)}
.quote-text{font-size:17px;color:var(--muted);line-height:1.5;margin-top:22px;position:relative;padding:0 18px}
.quote-mark{position:absolute;font-size:54px;color:#cfcfcf;line-height:1}
.quote-mark.open{left:-6px;top:-18px}
.quote-mark.close{right:-8px;bottom:-30px}
.intro-copy{position:absolute;left:487px;top:50px;width:590px}
.intro-copy h2{font-weight:400;font-size:30px}
.intro-copy p{font-size:14px;color:var(--muted);line-height:1.9;margin-top:10px}
.intro-copy p + p{margin-top:0}

.credibility{position:absolute;left:128px;top:790px;width:942px;height:250px;background:var(--panel)}
.accredited{position:absolute;left:62px;top:80px;width:168px;height:62px;background:var(--navy);border-radius:6px;display:flex;align-items:center;gap:12px;padding:0 12px;color:var(--white);font-weight:700;font-size:14px;line-height:1.2}
.accredited-square{width:40px;height:42px;background:var(--white);border-radius:4px;flex:none}
.listing-badge{position:absolute;left:264px;top:68px;width:55px;height:86px;background:#5a9fd6;border:3px solid #cfe3f5}
.history{position:absolute;left:363px;top:92px;color:var(--blue);font-size:22px;line-height:1.15;font-weight:600}
.endorse{position:absolute;left:487px;top:68px;width:420px}
.endorse p{font-size:21px;line-height:1.4;color:#444}
.btn-red{width:136px;height:34px;background:var(--red);font-size:11px;margin-top:16px}

.reviews{position:absolute;top:1080px;left:0;width:1200px;height:150px}
.review{position:absolute;display:flex;gap:20px}
.review.one{left:170px}
.review.two{left:640px}
.avatar{width:132px;height:132px;border-radius:50%;background:radial-gradient(circle at 50% 45%,#d9c7b8 0%,#a89888 60%,#e6e6e6 100%);flex:none;border:4px solid #f2f2f2}
.review-body{padding-top:10px;width:270px}
.review-name{font-size:16px}
.review-text{font-size:12.5px;color:#666;line-height:1.6;margin-top:4px}

.divider{position:absolute;top:1270px;left:118px;width:966px;height:1px;background:var(--line)}

.services{position:absolute;top:1305px;left:0;width:1200px}
.services h2{text-align:center;font-weight:400;font-size:29px}
.service{position:absolute;top:64px;width:270px}
.service.s1{left:125px}.service.s2{left:478px}.service.s3{left:830px}
.service-icon{height:56px}
.service h3{font-weight:400;color:var(--blue);font-size:20px;line-height:1.15;margin-top:10px}
.service p{font-size:13px;color:#777;line-height:1.6;margin-top:14px}
.btn-learn{width:112px;height:34px;background:var(--blue);font-size:11px;margin-top:18px}

.stations{position:absolute;top:1708px;left:130px;width:940px;display:flex;justify-content:space-between;align-items:center}
.station{font-weight:700;font-size:19px;color:#8d8d8d;text-align:center;line-height:1.05;width:118px}

.video-band{position:absolute;top:1806px;left:0;width:1200px;height:446px;background:var(--grey-bg)}
.video-band h2{text-align:center;font-weight:400;font-size:29px;margin-top:34px}
.video-frame{position:absolute;left:321px;top:98px;width:545px;height:318px;border:4px solid var(--white);background:linear-gradient(180deg,#6e6e6b 0%,#4b4b49 55%,#2e3235 100%)}
.play{position:absolute;left:232px;top:115px}

.newsletter{position:absolute;top:2252px;left:0;width:1200px;height:125px;background:var(--blue);display:flex;align-items:center;padding-left:118px}
.newsletter h2{color:var(--white);font-weight:400;font-size:29px;width:430px}
.email-field{width:302px;height:42px;background:var(--white);font-size:15px;color:#999;display:flex;align-items:center;padding-left:16px}
.btn-subscribe{width:141px;height:42px;background:var(--navy-deep);font-size:17px;font-weight:600;text-transform:none;margin-left:8px}

.contact{position:absolute;top:2377px;left:0;width:1200px;height:191px}
.contact-col{position:absolute;top:58px;font-size:17px;color:#555;line-height:1.4}
.contact-col .label{color:var(--ink);margin-bottom:6px}
.contact-col .value{color:var(--muted)}
.c1{left:103px}.c2{left:378px}.c3{left:592px}.c4{left:835px}
.contact-rule{position:absolute;top:56px;width:1px;height:88px;background:var(--line)}
.social{display:flex;gap:8px;margin-top:2px}
.social span{display:inline-flex;align-items:center;justify-content:center;width:32px;height:32px;border:1.5px solid var(--blue);border-radius:50%;color:var(--blue);font-size:8px;font-weight:700}

.footer-nav{position:absolute;top:2568px;left:0;width:1200px;height:57px;background:var(--navy);display:flex;justify-content:center;align-items:center;gap:58px;color:var(--white);font-size:16px}
.copyright{position:absolute;top:2625px;left:0;width:1200px;height:50px;background:var(--navy-deep);color:#aac3da;font-size:13px;display:flex;align-items:center;justify-content:center}
</style>
</head>
<body>

<header class="site-header">
  <a class="brand" href="#"><span class="brand-square"></span>Haven Quill</a>
  <nav class="main-nav">
    <a class="active" href="#">HOME</a><a href="#">ABOUT</a><a href="#">SERVICES</a><a href="#">TESTIMONIALS</a><a href="#">FAQ'S</a><a href="#">CONTACT</a>
  </nav>
  <a class="header-phone" href="#">
    <svg width="18" height="18" viewBox="0 0 24 24"><path fill="#fff" d="M6.6 10.8a15 15 0 0 0 6.6 6.6l2.2-2.2a1 1 0 0 1 1-.25 11.4 11.4 0 0 0 3.6.57 1 1 0 0 1 1 1V20a1 1 0 0 1-1 1A17 17 0 0 1 3 4a1 1 0 0 1 1-1h3.5a1 1 0 0 1 1 1c0 1.25.2 2.45.57 3.57a1 1 0 0 1-.25 1z"/></svg>
    (888) 555-0142
  </a>
</header>

<section class="hero">
  <div class="hero-portrait" role="img" aria-label="Portrait of the endorsing radio host in a dark suit"></div>
  <div class="hero-copy">
    <h1>Get Rid Of Your Timeshare<br>Permanently</h1>
    <p>Haven Quill is the Nation's most trusted timeshare release program and is backed by National Ledger best selling author Dana Whitcombe.</p>
    <a class="btn btn-hero" href="#">Call to action</a>
  </div>
</section>

<section class="intro">
  <div class="quote-card">
    <div class="quote-name">Aaron M.</div>
    <div class="quote-role">Former Club Marlowe owner</div>
    <p class="quote-text"><span class="quote-mark open">“</span>All persons in getting our timeshare switched over acted very professionally and my wife and I are so grateful to have this out of our name.<span class="quote-mark close">”</span></p>
  </div>
  <div class="intro-copy">
    <h2>Midwestern Pride, Rockford Proud</h2>
    <p>Here at Haven Quill, we take absolute and undeniable pride in our hometown, Rockford, Illinois. The fact that we are a Midwestern company has been one of our biggest assets attributed to earning the trust of our customers throughout the nation. In the heartland of America, we care and have compassion in areas that our competitors do not.</p>
    <p>We adhere to honesty, integrity and hard work in both life, and in business. America is a great nation and its citizens are just as great, which is why we believe that every single person in this nation who wants timeshare freedom can obtain it.</p>
  </div>
</section>

<section class="credibility">
  <div class="accredited"><span class="accredited-square"></span>QVR<br>ACCREDITED</div>
  <div class="listing-badge" role="img" aria-label="Trusted listing badge"></div>
  <div class="history">5-year<br>History</div>
  <div class="endorse">
    <p>The endorsements we have acquired from well known financial literacy figures</p>
    <a class="btn btn-red" href="#">Call to action</a>
  </div>
</section>

<section class="reviews">
  <div class="review one">
    <div class="avatar" role="img" aria-label="Photo of customer Alfred"></div>
    <div class="review-body">
      <div class="review-name">Alfred/Eileen C.</div>
      <p class="review-text">"...impressed overall with the final outcome and consistent updates received along the way to achievement, as well as no hidden fees or add-ones to originally agreed to terms"</p>
    </div>
  </div>
  <div class="review two">
    <div class="avatar" role="img" aria-label="Photo of customer Bob"></div>
    <div class="review-body">
      <div class="review-name">Bob M.</div>
      <p class="review-text">"Your sales rep was easy to talk to and conveyed honesty and trust. The fact that Haven Quill was willing to negotiate and discount the final price was a big factor"</p>
    </div>
  </div>
</section>

<div class="divider"></div>

<section class="services">
  <h2>Our Services</h2>
  <article class="service s1">
    <svg class="service-icon" width="60" height="56" viewBox="0 0 60 56"><rect x="4" y="6" width="52" height="36" fill="none" stroke="#e21b1b" stroke-width="3"/><rect x="12" y="13" width="16" height="20" fill="#e21b1b"/><line x1="32" y1="16" x2="48" y2="16" stroke="#e21b1b" stroke-width="3"/><line x1="32" y1="24" x2="48" y2="24" stroke="#e21b1b" stroke-width="3"/><line x1="22" y1="50" x2="38" y2="50" stroke="#e21b1b" stroke-width="3"/></svg>
    <h3>Sign up for a FREE<br>Consultation</h3>
    <p>Sign up for a FREE Consultation today and one of our specialized Intake Managers will speak with you about your options to legally and permanently terminate your timeshare mortgage. If you qualify for this attorney backed mortgage release service</p>
    <a class="btn btn-learn" href="#">Learn more</a>
  </article>
  <article class="service s2">
    <svg class="service-icon" width="60" height="56" viewBox="0 0 60 56"><line x1="30" y1="4" x2="30" y2="48" stroke="#e21b1b" stroke-width="3"/><line x1="8" y1="12" x2="52" y2="12" stroke="#e21b1b" stroke-width="3"/><path d="M4 30 L12 14 L20 30 Z M40 30 L48 14 L56 30 Z" fill="none" stroke="#e21b1b" stroke-width="2.5"/><path d="M4 30 a8 6 0 0 0 16 0 M40 30 a8 6 0 0 0 16 0" fill="#e21b1b"/><rect x="18" y="48" width="24" height="5" fill="#e21b1b"/></svg>
    <h3>The Attorneys Go<br>To Work</h3>
    <p>Sign up for a FREE Consultation today and one of our specialized Intake Managers will speak with you about your options to legally and permanently terminate your timeshare mortgage. If you qualify for this attorney backed mortgage release service</p>
    <a class="btn btn-learn" href="#">Learn more</a>
  </article>
  <article class="service s3">
    <svg class="service-icon" width="60" height="60" viewBox="0 0 60 60"><circle cx="30" cy="22" r="19" fill="#e21b1b"/><circle cx="30" cy="22" r="11" fill="none" stroke="#fff" stroke-width="3"/><path d="M18 36 L12 56 L22 50 L26 58 L30 42 Z M42 36 L48 56 L38 50 L34 58 L30 42 Z" fill="#e21b1b"/></svg>
    <h3>Guaranteed Contract<br>Termination</h3>
    <p>Sign up for a FREE Consultation today and one of our specialized Intake Managers will speak with you about your options to legally and permanently terminate your timeshare mortgage. If you qualify for this attorney backed mortgage release service</p>
    <a class="btn btn-learn" href="#">Learn more</a>
  </article>
</section>

<div class="stations">
  <span class="station">KVRA 94.9</span>
  <span class="station">Heartland Talk</span>
  <span class="station">KORV 570</span>
  <span class="station">Liberty 980</span>
  <span class="station">WQEL</span>
  <span class="station">Beacon 107.3</span>
  <span class="station">WRVN 88.1</span>
</div>

<section class="video-band">
  <h2>Watch Our Latest Video</h2>
  <div class="video-frame" role="img" aria-label="Video still of a couple sitting on a bench facing the sea">
    <svg class="play" width="80" height="80" viewBox="0 0 80 80"><circle cx="40" cy="40" r="40" fill="#fff"/><path d="M32 24 L58 40 L32 56 Z" fill="#111"/></svg>
  </div>
</section>

<section class="newsletter">
  <h2>Want to Join Our Newsletter</h2>
  <div class="email-field">Email address</div>
  <a class="btn btn-subscribe" href="#">Subscribe</a>
</section>

<section class="contact">
  <div class="contact-col c1"><div class="label">Haven Quill</div><div class="value">4120 Alder Rd #2b<br>Rockford, IL 61109</div></div>
  <div class="contact-rule" style="left:320px"></div>
  <div class="contact-col c2"><div class="label">Phone Number:</div><div class="value">888-555-0142<br>888-555-0178</div></div>
  <div class="contact-rule" style="left:560px"></div>
  <div class="contact-col c3"><div class="label">Fax Number:</div><div class="value">815-555-0126</div></div>
  <div class="contact-rule" style="left:775px"></div>
  <div class="contact-col c4"><div class="label">Get in Touch</div>
    <div class="social"><span>Chirp</span><span>Facet</span><span>Linkr</span><span>Plus</span></div>
  </div>
</section>

<nav class="footer-nav">
  <a href="#">HOME</a><a href="#">ABOUT</a><a href="#">SERVICES</a><a href="#">TESTIMONIALS</a><a href="#">FAQ'S</a><a href="#">CONTACT</a>
</nav>
<div class="copyright">© 2017 Company Name &nbsp;All right reserved &nbsp;Term of Use</div>

</body>
</html>
```